PowerPoint Design Project

We need a powerpoint design for our consulting company, Brindle Consulting. We provide technology strategy and solutioning services, with an emphasis on cloud technology. More information about our services can be found at www.brindleconsulting-example.com

We are looking for a design that is professional, but not corporate stuffy. The design needs to use our primary colors in our brand.
Updates

Reason: We need to iterate on some of the great designs, plus, many people have not had a chance to submit their design yet.

Reason: We had a lot of people accept the project, but not all of them have responded yet. We wanted to get them some time, plus, ask a couple of people to make some minor revisions.

Target Market(s)

Technology buyers between the ages of 30-55 at Vantor 1000 companies

Industry/Entity Type

It Company

Requirements
Must have
• Must follow our logo colors.
Must have at least a cover slide and interior content slide.
Should not have
• Should not contain anything cartoonish or anything with lots of clouds

```html
<!DOCTYPE html>
<html lang="en">
<head>
<meta charset="utf-8">
<title>Brindle Consulting — Content</title>
<link href="https://fonts.googleapis.com/css2?family=Arimo:wght@400&family=Lato:wght@400&display=swap" rel="stylesheet">
<style>
  :root {
    --header-bg: #5d5449;
    --header-dots: #8b8379;
    --footer-bg: #2d5481;
    --canvas-bg: #ffffff;
    --heading-blue: #2f5c90;
    --bullet-blue: #2f5c90;
    --body-gray: #555555;
    --white: #ffffff;
  }
  html, body {
    margin: 0;
    padding: 0;
    overflow: hidden;
    background: var(--canvas-bg);
  }
  .slide {
    position: relative;
    width: 1200px;
    height: 900px;
    overflow: hidden;
    background: var(--canvas-bg);
    font-family: "Lato", "Gill Sans", sans-serif;
  }
  .slide-header {
    position: absolute;
    left: 0; top: 0;
    width: 1200px;
    height: 225px;
    background: var(--header-bg);
  }
  .header-texture {
    position: absolute;
    left: 70px; top: 0;
    width: 340px;
    height: 225px;
    background: radial-gradient(ellipse at 35% 40%, rgba(139,131,121,0.75) 0%, rgba(139,131,121,0.35) 45%, rgba(93,84,73,0) 75%);
  }
  .slide-title {
    position: absolute;
    left: 0; top: 110px;
    width: 1200px;
    margin: 0;
    text-align: center;
    font-family: "Arimo", "Helvetica", sans-serif;
    font-weight: 400;
    font-size: 68px;
    line-height: 1;
    color: var(--white);
  }
  .topic-column {
    position: absolute;
    top: 340px;
    width: 480px;
    margin: 0;
    padding: 0;
    list-style: none;
  }
  .topic-column.left { left: 93px; }
  .topic-column.right { left: 600px; }
  .topic {
    position: relative;
    padding-left: 62px;
    margin-bottom: 26px;
  }
  .topic::before {
    content: "";
    position: absolute;
    left: 5px; top: 16px;
    width: 11px; height: 11px;
    border-radius: 50%;
    background: var(--bullet-blue);
  }
  .topic-name {
    display: block;
    font-size: 38px;
    line-height: 46px;
    color: var(--heading-blue);
  }
  .subtopics {
    list-style: none;
    margin: 0;
    padding: 0;
  }
  .subtopics li {
    position: relative;
    padding-left: 60px;
    font-size: 25px;
    line-height: 37px;
    color: var(--body-gray);
  }
  .subtopics li::before {
    content: "\2013";
    position: absolute;
    left: 8px;
    color: var(--body-gray);
  }
  .slide-footer {
    position: absolute;
    left: 0; top: 840px;
    width: 1200px;
    height: 60px;
    background: var(--footer-bg);
  }
  .footer-url {
    position: absolute;
    right: 105px; top: 15px;
    font-size: 25px;
    line-height: 30px;
    color: var(--white);
  }
</style>
</head>
<body>
  <main class="slide">
    <header class="slide-header">
      <div class="header-texture" role="img" aria-label="Cluster of soft grey dots as header decoration"></div>
      <h1 class="slide-title">Content</h1>
    </header>

    <ul class="topic-column left">
      <li class="topic">
        <span class="topic-name">Services</span>
        <ul class="subtopics">
          <li>Management Consulting</li>
          <li>IT Consulting</li>
        </ul>
      </li>
      <li class="topic">
        <span class="topic-name">Solutions</span>
        <ul class="subtopics">
          <li>Business Applications</li>
          <li>Web &amp; Mobile</li>
        </ul>
      </li>
    </ul>

    <ul class="topic-column right">
      <li class="topic">
        <span class="topic-name">Services</span>
        <ul class="subtopics">
          <li>Management Consulting</li>
          <li>IT Consulting</li>
        </ul>
      </li>
      <li class="topic">
        <span class="topic-name">Solutions</span>
        <ul class="subtopics">
          <li>Business Applications</li>
          <li>Web &amp; Mobile</li>
        </ul>
      </li>
    </ul>

    <footer class="slide-footer">
      <span class="footer-url">www.brindleconsulting-example.com</span>
    </footer>
  </main>
</body>
</html>
```